Flyer-Design
Sehr flexibel bei Änderungswünschen. Herzlichen Dank. Würde jederzeit wieder mit Bettina zusammenarbeiten.
Zielgruppe
Wir sind eine eine Praxis und unsere Zielgruppe sind Kunden. Es sollte einen Faltflyer geben, welcher Doppelseitig bedruckt wird.
Aufgabenstellung
Ich habe genaue Vorstellungen, wie dieser Flyer aussehen soll. Jedoch bin ich auch auf neue Ideen gespannt :). Wunschvorstellung wäre ein Falzflyer (siehe Bild Musterfyler). Des weiteren habe ich ein Word gemacht, mit dem gesamten Inhalt des Textes und wie der Flyer am Besten aufgebaut werden sollte. (siehe Flyer Tierversicherung).
Die beiden letzten Abschnitte (Tipp an unsere Kunden, Fazit) sollten ein wenig auffallen. Müssen auch nicht am Schluss sein.
Des weiteren wäre ich dankbar, wenn das CI/CD der Unternehmung berücksichtig wird. Bitte werfen Sie einen Blick auf die Webseite www.felgor-tieraerzte.ch. Ein Logo ist ebenfalls im Anhang. Bei Fragen bitte melden.
Ich freue mich auf Vorschläge.

```html
<!DOCTYPE html>
<html lang="de">
<head>
<meta charset="utf-8">
<title>Faltflyer Tierversicherungen – Felgor Tierärzte</title>
<link href="https://fonts.googleapis.com/css2?family=Arimo:wght@400;700&display=swap" rel="stylesheet">
<style>
  :root{
    --bg:#ffffff;
    --maroon-dark:#5a0a1c;
    --maroon:#7a0f28;
    --red:#a8102f;
    --crimson:#c8153f;
    --pink:#d01c50;
    --white:#ffffff;
    --text-light:#f6dde3;
    --rule:rgba(255,255,255,.55);
  }
  *{box-sizing:border-box;margin:0;padding:0}
  html,body{width:1200px;height:2970px;overflow:hidden;background:var(--bg)}
  body{font-family:"Arimo",Arial,sans-serif;color:var(--white);position:relative}

  .spread{position:absolute;left:0;width:1200px;height:848px;display:flex}
  .spread--outside{top:425px}
  .spread--inside{top:1698px}
  .panel{position:relative;width:400px;height:848px;overflow:hidden}

  /* outside: inner flap */
  .flap{background:linear-gradient(180deg,var(--crimson) 0%,var(--red) 45%,var(--maroon-dark) 100%)}
  .flap__photo{position:absolute;left:0;top:0;width:400px;height:350px;background:linear-gradient(160deg,#d8d3cc 0%,#9e938a 45%,#3a3432 100%)}
  .flap__text{position:absolute;left:26px;right:26px;top:378px;font-size:13px;line-height:1.32;text-align:justify;color:var(--text-light)}
  .flap__text p{margin-bottom:11px}

  /* outside: back panel */
  .back{background:linear-gradient(180deg,var(--maroon) 0%,var(--maroon-dark) 100%)}
  .back__deco{position:absolute;inset:0}
  .back__content{position:absolute;left:26px;right:20px;top:436px}
  .back h2{font-size:25px;font-weight:400;margin-bottom:12px}
  .hours{display:grid;grid-template-columns:86px 1fr;font-size:14px;line-height:1.6;color:var(--text-light)}
  .back__note{font-size:14px;line-height:1.35;margin-top:4px;color:var(--text-light)}
  .contact{margin-top:58px}
  .contact p{font-size:14px;line-height:1.35;font-weight:700}

  /* outside: cover */
  .cover{background:var(--red)}
  .cover__art{position:absolute;inset:0}
  .cover__title{position:absolute;left:0;right:0;top:596px;text-align:center;font-size:24px;line-height:1.3}
  .cover__title strong{display:block;font-size:33px;font-weight:400;margin-top:6px}
  .cover__brand{position:absolute;left:0;right:0;top:732px;height:86px;background:var(--white);display:flex;align-items:center;justify-content:center}
  .brand{color:var(--crimson);font-size:22px;font-weight:400;letter-spacing:2px;line-height:1.05;text-align:center}

  /* inside */
  .inside{background:linear-gradient(180deg,var(--maroon) 0%,var(--maroon-dark) 55%,var(--maroon) 100%)}
  .inside__body{position:absolute;left:26px;right:24px;top:22px;font-size:12.4px;line-height:1.28;color:var(--text-light)}
  .letter{display:flex;align-items:flex-end;gap:6px;font-size:15px;color:var(--white);margin-top:8px}
  .letter::after{content:"";flex:1;border-bottom:1px solid var(--rule);margin-bottom:3px}
  .inside h3{font-size:13px;font-weight:700;color:var(--white);margin-top:5px}
  .inside p{text-align:justify;margin-bottom:6px}
  .lead{font-size:14px;line-height:1.3}
  .tip{position:absolute;left:0;right:0;bottom:0;height:318px;background:var(--pink);padding:22px 26px;font-size:12.4px;line-height:1.3}
  .tip__head{display:flex;align-items:center;gap:7px;font-size:14px;margin-bottom:12px}
  .tip h3{margin-top:8px}
</style>
</head>
<body>

<section class="spread spread--outside" aria-label="Aussenseite">
  <div class="panel flap">
    <div class="flap__photo" role="img" aria-label="Foto: Katze mit Halskrause liegt auf einem Kissen"></div>
    <div class="flap__text">
      <p>Haustiere sind für viele von uns von grosser Bedeutung und sensible Weggefährten, mit denen sich lachen, reden und auch einmal weinen lässt. Neben den vielen Vorzügen, die ein eigenes Haustier mit sich bringen, können diese auch krank werden oder einen Unfall haben.</p>
      <p>Wenn eine Behandlung das geliebte Haustier retten kann, jedoch hohe Kosten für Medikamente, Behandlungen, Operationen oder Klinikaufenthalte auslöst, dann entstehen bei vielen Personen ernsthafte Sorgen und Belastungen, denen allerdings vorgebeugt werden kann.</p>
      <p>Mit einem Abschluss einer Tierversicherung gegen Unfall und Krankheit können verschiedene Vorkehrungen getroffen werden, um hohe Kosten im Ernstfall zu reduzieren.</p>
      <p>Daher ist es wichtig, dass man sich vorgängig über die Möglichkeiten einer Tierversicherung gegen Unfall und Krankheit informiert, um bestmöglich vorbereitet zu sein, sollte es dem treuen Begleiter einmal schlecht gehen.</p>
      <p>In diesem Flyer finden Sie alles von A-Z, was sie über Tierversicherungen gegen Unfall und Krankheit wissen müssen.</p>
    </div>
  </div>

  <div class="panel back">
    <svg class="back__deco" width="400" height="848" viewBox="0 0 400 848" aria-hidden="true">
      <defs>
        <linearGradient id="band" x1="0" y1="0" x2="0" y2="1">
          <stop offset="0" stop-color="#c8153f"/><stop offset="1" stop-color="#8e0d2b"/>
        </linearGradient>
      </defs>
      <polygon points="0,40 70,0 270,560 230,600" fill="url(#band)" opacity=".85"/>
      <polygon points="400,200 400,330 280,640 240,600" fill="url(#band)" opacity=".85"/>
      <path d="M230,600 Q250,640 280,640" fill="none" stroke="#d01c50" stroke-width="3"/>
    </svg>
    <div class="back__content">
      <h2>Öffnungszeiten</h2>
      <div class="hours">
        <span>Mo bis Fr:</span><span>8.00 – 12.00 und</span>
        <span></span><span>13.30 - 18.00 Uhr</span>
        <span>Sa:</span><span>8.00 – 12.00 Uhr</span>
      </div>
      <p class="back__note">Dringende Notfälle auch ausserhalb der Kliniköffnungszeiten.</p>
      <div class="contact">
        <h2>Kontakt</h2>
        <p>Felgor Tierärzte | Kleintier AG / Grosstier AG</p>
        <p>Lindenweg 8 | 6430 Schwyz</p>
        <p>Tel.: 041 555 01 23</p>
        <p>Web: http://www.felgor-tieraerzte.ch</p>
      </div>
    </div>
  </div>

  <div class="panel cover">
    <svg class="cover__art" width="400" height="848" viewBox="0 0 400 848">
      <defs>
        <linearGradient id="photo" x1="0" y1="0" x2="1" y2="1">
          <stop offset="0" stop-color="#e4e2de"/><stop offset=".5" stop-color="#8a6a52"/><stop offset="1" stop-color="#3b2e28"/>
        </linearGradient>
        <linearGradient id="redfill" x1="0" y1="0" x2="0" y2="1">
          <stop offset="0" stop-color="#c8153f"/><stop offset="1" stop-color="#7a0f28"/>
        </linearGradient>
      </defs>
      <rect width="400" height="848" fill="url(#redfill)"/>
      <polygon points="0,0 400,0 400,260 200,560 0,240" fill="url(#photo)" role="img" aria-label="Foto: Frau mit Maske umarmt ihren Hund"/>
      <polyline points="0,240 200,560 400,260" fill="none" stroke="#d01c50" stroke-width="10"/>
    </svg>
    <h1 class="cover__title">Tierversicherungen gegen<br>Unfall und Krankheit:<strong>Fluch oder Segen?</strong></h1>
    <div class="cover__brand"><div class="brand">FELGOR<br>TIERÄRZTE</div></div>
  </div>
</section>

<section class="spread spread--inside" aria-label="Innenseite">
  <div class="panel inside">
    <div class="inside__body">
      <div class="letter">A</div>
      <h3>Abschluss</h3>
      <p class="lead">Beim Abschluss einer Versicherung muss das Tier jung und gesund sein.</p>
      <h3>Anbieter</h3>
      <p>Auf dem Schweizer Markt gibt verschiedene Anbieter von Tierversicherungen wie beispielsweise Tierwohl, Pfotenschutz, Alpina, Heliora und Generis.</p>
      <p>Wir empfehlen keinen konkreten Anbieter, da es viele verschiedene unterschiedliche Produkte auf dem Markt gibt und jeder Kunde andere Wünsche und ein anderes Budget hat. Unseres Erachtens liegen die Unterschiede im Detail.</p>
      <h3>Altersbegrenzung</h3>
      <p>Die Anbieter von Tierversicherungen haben Altersbegrenzungen, üblicherweise betragen diese fünf Jahre bei Katzen und sechs Jahre bei Hunden.</p>
      <h3>Arztwahl</h3>
      <p>Gewisse Versicherungen erlauben keine freie Tierarztwahl. Sichern Sie sich bei Vertragsabschluss ab und fragen, sie explizit nach.</p>
      <h3>Aufnahmealter</h3>
      <p>Die Versicherungsanbieter nehmen die Tiere in der Regel im Alter von 3 Monaten auf. Wir empfehlen die Tiere so früh wie möglich zu versichern.</p>
      <h3>Ausschlüsse</h3>
      <p>Beachten sie, ob Ausschlüsse aus einer Versicherungsleistung existieren und ob diese für sie von Bedeutung sind.</p>
      <div class="letter">G</div>
      <h3>Geburtskrankheiten/Erbkrankheiten</h3>
      <p>Diese werden bei vielen Angeboten ausgeschlossen oder müssen explizit dazu versichert werden.</p>
      <div class="letter">I</div>
      <h3>Impfungen</h3>
      <p>Nur wenige Anbieter übernehmen auch Impfungen. Fall ein Anbieter diese Leistung übernimmt, hat er in der Regel einen maximalen Betrag festgelegt.</p>
      <div class="letter">K</div>
      <h3>Karenzfrist</h3>
      <p>Bei Versicherungen besteht jeweils eine Wartezeit, die</p>
    </div>
  </div>

  <div class="panel inside">
    <div class="inside__body">
      <p>zwischen Unterzeichnung der Police und einem Deckungsanspruch eingehalten werden muss. In der Regel beträgt diese für nicht-chronische Krankheiten einen Monat und bei chronischen Krankheiten drei Monate. Bei einem Unfall gibt es in der Regel keine Karenzfrist oder je nach Anbieter bis zu einem Monat.</p>
      <div class="letter">L</div>
      <h3>Leistungen</h3>
      <p>Die inkludierten Leistungen und die gebotene Abdeckung ist genau zu prüfen. Übernimmt der Versicherungsanbieter alle Behandlungen oder sind zum Beispiel chronische Krankheiten oder Erbkrankheiten ausgeschlossen. Ein Blick auf das Kleingedruckte beim Versicherungsangebot lohnt sich.</p>
      <p>Sie können ihr Tier entweder gegen Krankheit oder gegen Unfall oder gegen beides versichern, letzteres empfehlen wir Ihnen.</p>
      <div class="letter">P</div>
      <h3>Prämien</h3>
      <p>Die Prämien der einzelnen Anbieter fallen unterschiedlich aus, deshalb ist es wichtig Versicherungsangebote zu vergleichen, um den passenden Tarif für ihr Haustier zu finden.</p>
      <h3>Prämienerhöhung</h3>
      <p>Es gibt Versicherungen, die während der Laufzeit die Prämien erhöhen, andere bieten einen Pauschalbetrag an, damit Planungssicherheit geboten wird.</p>
    </div>
    <aside class="tip">
      <div class="tip__head">
        <svg width="16" height="16" viewBox="0 0 16 16" aria-hidden="true"><circle cx="8" cy="8" r="7" fill="none" stroke="#fff" stroke-width="1.3"/><rect x="7.3" y="6.8" width="1.4" height="5" fill="#fff"/><circle cx="8" cy="4.6" r=".9" fill="#fff"/></svg>
        <span>Tipp an unsere Kunden</span>
      </div>
      <p>Wir empfehlen Ihnen die die Tierarztkosten der letzten Jahre zusammenzustellen und zu prüfen, ob sie von der gewählten Versicherung übernommen worden wären. Bei diesem Vergleich darf aber der Selbstbehalt nicht ausser Acht gelassen werden.</p>
      <h3>Fazit</h3>
      <p>Wir von der Felgor Tierärzte AG haben bisher sehr gute Erfahrungen mit Tierversicherungen unserer Kunden gemacht. Wir empfehlen Ihnen jedoch etwas Zeit in die Auswahl einer für sie passenden Tierversicherung zu investieren.</p>
    </aside>
  </div>

  <div class="panel inside">
    <div class="inside__body">
      <h3>Preis</h3>
      <p>Langfristig ist billigste Vertragsoption oft nicht die beste, da einige Versicherungen mit einem günstigeren Preis starten und im Laufe der Jahre, wenn das Tier älter wird, den Tarif erhöht.</p>
      <div class="letter">R</div>
      <h3>Rabatte</h3>
      <p>Vereinzelte Versicherungsanbieter gewähren Rabatte, wenn in einem Versicherungsjahr keine Leistungen bezogen wurden.</p>
      <h3>Rechnungsstellung</h3>
      <p>Die erbrachten Leistungen durch den Tierarzt sind direkt vom Tierhalter zu bezahlen. Anschliessend kann die Rechnung beim Versicherungsanbieter eingereicht werden.</p>
      <div class="letter">S</div>
      <h3>Schadenfall</h3>
      <p>Wenn ein Schadensfall eintritt, direkt den Tierarzt aufsuchen und erst anschliessend den Fall bei der Versicherung melden und gleich die Kostenübernahme abklären. Die Rechnungskopie wird bei Behandlungsabschluss der Versicherung zu Prüfung und Begleichung weitergeleitet.</p>
      <h3>Selbstbehalt</h3>
      <p>Der Selbstbehalt gibt an, welche Kosten bei einem Versicherungsfall selbst zu tragen sind. Einige Anbieter bieten ebenfalls die Option mit CHF 0 an. Falls man bei der Prämie etwas sparen möchte, sollte der Selbstbehalt auf einen höheren Betrag festgelegt werden. Einige Versicherungsanbieter ziehen den Selbstbehalt bei jedem Krankheitsfall an und andere jährlich.</p>
      <div class="letter">V</div>
      <h3>Versicherungsende</h3>
      <p>Das Haustier ist solange versichert, wie der Halter die Prämien bezahlt und das Tier lebt.</p>
      <h3>Versicherungssumme</h3>
      <p>Dies ist der Höchstbetrag, den der Kunden von einem Versicherungsanbieter für eine Behandlung eines Haustieres erhält.</p>
      <h3>Vertragsdauer</h3>
      <p>Die Mindestlaufzeit von Tierversicherungen beträgt in der Regel ein Jahr.</p>
    </div>
  </div>
</section>

</body>
</html>
```